One business card required with 2 company logos and 2 people's details

One business card required.
No preference on design - One side could show the 2 different business logos for the companies we own. The reverse could have the details shown below.
Another option could be one business one side and one business on the reverse. Happy to receive designs.

Carol Denbigh
07700 318 274
Rachel Tolland
07700 582 036

website: truelymarvellous.example
email: info@truelymarvellous.example

website: ironwillowevents.example
email: info:ironwillowevents.example

May be nice to have icons instead of the words email/website?

I have included different versions of the logos to help with your design.

Contact Information for Business Card

see project overview

Requirements
Must have
• both company logos, both contact names and contact details

```html
<!DOCTYPE html>
<html lang="en">
<head>
<meta charset="utf-8">
<title>Business Card – Truely Marvellous &amp; Iron Willow Events</title>
<link href="https://fonts.googleapis.com/css2?family=Roboto:wght@400;500;700&display=swap" rel="stylesheet">
<style>
  :root {
    --backdrop: #1e1e1e;
    --sky-blue: #3f92d0;
    --deep-blue: #0a47a8;
    --bright-blue: #0ac4f5;
    --accent-blue: #1f6fe0;
    --accent-violet: #7b6fd0;
    --ink: #2a2740;
    --white: #ffffff;
  }
  html, body {
    margin: 0;
    width: 1200px;
    height: 1200px;
    overflow: hidden;
    background: var(--backdrop);
    font-family: "Roboto", Arial, sans-serif;
  }
  .card {
    position: absolute;
    left: 200px;
    width: 800px;
    height: 457px;
    border-radius: 22px;
    overflow: hidden;
    box-shadow: 0 24px 40px rgba(0,0,0,0.6);
  }
  .card--front { top: 87px; }
  .card--back { top: 656px; }
  .card__art { position: absolute; inset: 0; }
  .contact {
    position: absolute;
    color: var(--white);
    top: 124px;
  }
  .card--front .contact { left: 36px; }
  .card--back .contact { right: 45px; text-align: right; top: 124px; }
  .contact__name {
    font-weight: 500;
    font-size: 27px;
    line-height: 32px;
    margin: 0;
  }
  .contact__phone {
    font-size: 18px;
    line-height: 24px;
    margin: 0 0 14px;
    display: flex;
    align-items: center;
    gap: 5px;
  }
  .card--back .contact__phone { justify-content: flex-end; }
  .contact__phone svg { width: 14px; height: 14px; fill: var(--white); }
  .contact__web {
    font-size: 18px;
    line-height: 23px;
    margin: 22px 0 0;
  }
  .brand {
    position: absolute;
    display: flex;
    align-items: center;
    justify-content: center;
    gap: 12px;
    font-weight: 500;
    font-size: 30px;
    text-align: center;
    line-height: 36px;
  }
  .brand--marvellous {
    left: 440px; top: 160px; width: 280px;
    color: var(--ink);
  }
  .brand--willow {
    left: 60px; top: 180px; width: 290px;
    color: var(--accent-blue);
  }
  .brand__dot {
    width: 14px; height: 14px; border-radius: 50%;
    background: currentColor; flex: none;
  }
</style>
</head>
<body>

<section class="card card--front">
  <svg class="card__art" viewBox="0 0 800 457" width="800" height="457">
    <defs>
      <linearGradient id="front-edge" x1="0" y1="0" x2="0" y2="1">
        <stop offset="0" stop-color="#8a7fe0"/>
        <stop offset="1" stop-color="#2a4fc8"/>
      </linearGradient>
    </defs>
    <rect class="front-field" width="800" height="457" fill="var(--sky-blue)"/>
    <path class="front-edge" fill="url(#front-edge)"
      d="M406,0 C350,90 330,200 362,300 C400,385 470,430 500,457 L575,457 C500,430 410,380 370,300 C330,200 360,90 412,0 Z"/>
    <path class="front-panel" fill="var(--white)"
      d="M418,0 C368,90 340,200 372,298 C412,378 500,430 575,457 L800,457 L800,0 Z"/>
  </svg>

  <div class="contact">
    <p class="contact__name">Rachel Tolland</p>
    <p class="contact__phone"><svg viewBox="0 0 24 24"><path d="M6.6 10.8a15.1 15.1 0 0 0 6.6 6.6l2.2-2.2c.3-.3.7-.4 1-.2 1.1.4 2.3.6 3.6.6.6 0 1 .4 1 1V20c0 .6-.4 1-1 1A17 17 0 0 1 3 4c0-.6.4-1 1-1h3.5c.6 0 1 .4 1 1 0 1.3.2 2.5.6 3.6.1.3 0 .7-.2 1L6.6 10.8z"/></svg>07700 582 036</p>
    <p class="contact__name">Carol Denbigh</p>
    <p class="contact__phone"><svg viewBox="0 0 24 24"><path d="M6.6 10.8a15.1 15.1 0 0 0 6.6 6.6l2.2-2.2c.3-.3.7-.4 1-.2 1.1.4 2.3.6 3.6.6.6 0 1 .4 1 1V20c0 .6-.4 1-1 1A17 17 0 0 1 3 4c0-.6.4-1 1-1h3.5c.6 0 1 .4 1 1 0 1.3.2 2.5.6 3.6.1.3 0 .7-.2 1L6.6 10.8z"/></svg>07700 318 274</p>
    <p class="contact__web">info@truelymarvellous.example<br>www.truelymarvellous.example</p>
  </div>

  <div class="brand brand--marvellous"><span class="brand__dot"></span>Truely Marvellous</div>
</section>

<section class="card card--back">
  <svg class="card__art" viewBox="0 0 800 457" width="800" height="457">
    <defs>
      <radialGradient id="back-glow" cx="0.55" cy="0.58" r="0.6">
        <stop offset="0" stop-color="var(--bright-blue)"/>
        <stop offset="0.55" stop-color="#0a6fd8"/>
        <stop offset="1" stop-color="var(--deep-blue)"/>
      </radialGradient>
    </defs>
    <rect class="back-field" width="800" height="457" fill="url(#back-glow)"/>
    <path class="back-edge" fill="var(--accent-blue)"
      d="M230,457 C320,430 410,380 440,290 C460,200 440,80 392,0 L402,0 C458,80 472,200 452,300 C420,390 360,430 300,457 Z"/>
    <path class="back-panel" fill="var(--white)"
      d="M0,0 L392,0 C440,80 458,200 440,290 C410,380 320,430 230,457 L0,457 Z"/>
  </svg>

  <div class="brand brand--willow"><span class="brand__dot"></span>Iron Willow Events</div>

  <div class="contact">
    <p class="contact__name">Rachel Tolland</p>
    <p class="contact__phone">07700 582 036<svg viewBox="0 0 24 24"><path d="M6.6 10.8a15.1 15.1 0 0 0 6.6 6.6l2.2-2.2c.3-.3.7-.4 1-.2 1.1.4 2.3.6 3.6.6.6 0 1 .4 1 1V20c0 .6-.4 1-1 1A17 17 0 0 1 3 4c0-.6.4-1 1-1h3.5c.6 0 1 .4 1 1 0 1.3.2 2.5.6 3.6.1.3 0 .7-.2 1L6.6 10.8z"/></svg></p>
    <p class="contact__name">Carol Denbigh</p>
    <p class="contact__phone">07700 318 274<svg viewBox="0 0 24 24"><path d="M6.6 10.8a15.1 15.1 0 0 0 6.6 6.6l2.2-2.2c.3-.3.7-.4 1-.2 1.1.4 2.3.6 3.6.6.6 0 1 .4 1 1V20c0 .6-.4 1-1 1A17 17 0 0 1 3 4c0-.6.4-1 1-1h3.5c.6 0 1 .4 1 1 0 1.3.2 2.5.6 3.6.1.3 0 .7-.2 1L6.6 10.8z"/></svg></p>
    <p class="contact__web">info@truelymarvellous.example<br>www.truelymarvellous.example</p>
  </div>
</section>

</body>
</html>
```